Business card for Eyelash extension salon in Beverly Hills,California USA

We need new business card for our salon in Beverly Hills. The salon name is 'Lumarra' . We would like to have...Business name: Lumarra Name of person: will provide later Address 6128 N.Corbel Ridge Blvd Beverly Hills , CA 90210 Phone: will provide later (Text only) Web: www.lumarrastudio-example.com Pictogrid icon, Friendvale icon follow us for seasonal campaign and news @lumarrastudioexample Design should look elegant, high-end, clean, simple, cohesive with my brand. Please refer my brand board. Business name color will be metallic bronzy color. Im thinking grey background or white background. Thanks

Target Market(s)

25-35. Gender neutral. People who are in Entertainment business industry.
This is High-end Eyelash extension salon in Beverly Hills

Industry/Entity Type

Beauty Salon

Contact Information for Business Card

Business name: Lumarra
Name of person: will provide later
Address 6128 N.Corbel Ridge Blvd Beverly Hills , CA 90210
Phone: will provide later (Text only)
Web: www.lumarrastudio-example.com
Pictogrid icon, Friendvale icon
follow us for seasonal campaign and news @lumarrastudioexample

Requirements
Must have
• Beautiful, elegant, clean and simple look but very attractive and modern
Should not have
• We don't like too clutter, too busy designs.

```html
<!DOCTYPE html>
<html lang="en">
<head>
<meta charset="UTF-8">
<title>Lumarra Beverly Hills – Business Card</title>
<link rel="stylesheet" href="https://fonts.googleapis.com/css2?family=Cormorant+Garamond:ital,wght@0,400;0,500;1,400&family=Josefin+Sans:wght@400&display=swap">
<style>
  :root {
    --bronze: #84634b;
    --bronze-text: #8a6447;
    --paper: #ffffff;
    --ink: #2a2320;
    --backdrop: #efe9e4;
  }
  * { box-sizing: border-box; margin: 0; padding: 0; }
  html, body { width: 1200px; height: 800px; overflow: hidden; }
  body {
    position: relative;
    background: var(--backdrop);
    font-family: "Cormorant Garamond", Georgia, serif;
  }
  .card {
    position: absolute;
    width: 500px;
    height: 286px;
    box-shadow: 0 6px 14px rgba(60, 40, 30, 0.18);
  }
  .card--back {
    left: 150px;
    top: 120px;
    background: var(--bronze);
    color: var(--paper);
  }
  .card--front {
    left: 500px;
    top: 430px;
    background: var(--paper);
    color: var(--ink);
    border-bottom: 6px solid var(--bronze);
  }
  .brand {
    position: absolute;
    left: 0; right: 0;
    text-align: center;
  }
  .brand__name {
    display: block;
    font-weight: 400;
    letter-spacing: 2px;
    line-height: 1;
  }
  .brand__place {
    display: block;
    font-family: "Josefin Sans", Arial, sans-serif;
    letter-spacing: 3px;
    margin-top: 8px;
  }
  .card--back .brand { top: 62px; }
  .card--back .brand__name { font-size: 78px; }
  .card--back .brand__place { font-size: 10px; }
  .card--front .brand { top: 40px; color: var(--bronze-text); }
  .card--front .brand__name { font-size: 66px; }
  .card--front .brand__place { font-size: 8px; }

  .follow {
    position: absolute;
    left: 0; right: 0;
    bottom: 26px;
    text-align: center;
    font-style: italic;
  }
  .follow__lead {
    font-size: 12px;
    text-decoration: underline;
    text-underline-offset: 2px;
  }
  .follow__channels {
    margin-top: 6px;
    display: flex;
    justify-content: center;
    align-items: center;
    gap: 10px;
    font-size: 12px;
  }
  .channel { display: inline-flex; align-items: center; gap: 4px; font-style: normal; }
  .channel__dot {
    width: 9px; height: 9px; border-radius: 50%;
    background: var(--paper);
  }

  .contact {
    position: absolute;
    left: 30px;
    bottom: 26px;
    list-style: none;
    font-size: 12px;
  }
  .contact li { display: flex; align-items: center; gap: 7px; margin-top: 8px; }
  .contact svg { width: 13px; height: 11px; fill: var(--ink); }
  .contact__address {
    color: var(--bronze-text);
    font-style: italic;
    margin-top: 6px;
  }
  .person {
    position: absolute;
    right: 36px;
    bottom: 56px;
    text-align: right;
  }
  .person__name { font-style: italic; font-size: 17px; color: var(--bronze-text); }
  .person__role { font-size: 11px; }
</style>
</head>
<body>

<section class="card card--back" aria-label="Card back">
  <div class="brand">
    <span class="brand__name">Lumarra</span>
    <span class="brand__place">BEVERLY HILLS</span>
  </div>
  <div class="follow">
    <p class="follow__lead">Follow us for seasonal campaign and news:</p>
    <p class="follow__channels">
      <span class="channel"><span class="channel__dot"></span>Pictogrid</span>
      <span class="channel"><span class="channel__dot"></span>Friendvale</span>
      <span class="follow__handle">@lumarrastudioexample</span>
    </p>
  </div>
</section>

<section class="card card--front" aria-label="Card front">
  <div class="brand">
    <span class="brand__name">Lumarra</span>
    <span class="brand__place">BEVERLY HILLS</span>
  </div>
  <ul class="contact">
    <li>
      <svg viewBox="0 0 13 11" aria-hidden="true"><path d="M1 3.5C1 1.5 4 1 6.5 1S12 1.5 12 3.5L10 4.5 9 3H4L3 4.5Z"/><rect x="2.5" y="5" width="8" height="5" rx="1"/></svg>
      (+000)555-0142
    </li>
    <li>
      <svg viewBox="0 0 13 11" aria-hidden="true"><rect x="0.5" y="1" width="12" height="9"/><path d="M1 1.5 6.5 6 12 1.5" fill="none" stroke="#fff" stroke-width="1.2"/></svg>
      dana@lumarrastudio-example.com
    </li>
    <li>
      <svg viewBox="0 0 13 11" aria-hidden="true"><path d="M5 8 3.5 9.5a2 2 0 0 1-3-3L2 5M8 3l1.5-1.5a2 2 0 0 1 3 3L11 6M4.5 6.5l4-4" fill="none" stroke="#2a2320" stroke-width="1.3" stroke-linecap="round"/></svg>
      www.lumarrastudio-example.com
    </li>
    <li class="contact__address">6128 N.Corbel Ridge Blvd Beverly Hills , CA 90210</li>
  </ul>
  <div class="person">
    <p class="person__name">Dana Whitfield</p>
    <p class="person__role">Owner / Founder</p>
  </div>
</section>

</body>
</html>
```